BrightFern Web Design Project

BrightFern IT solutions, a IT mananaged services company is looking to redesign current website (brightfernsolutions.example).

The website should convey professionalism within the managed it services community. The layout should invite users to explore other areas of the site. Should contain tools and other current information that clients or potential clients would find useful. Product pages, special offers and informational pages should be easily editable by non-programmers. Tidewarden.example is a good site to review as an example of the design components we like.

Target Market(s)

Professional services companies with 10-100 users

Industry/Entity Type

It Company

Requirements
Must have
• • Clickable icons and graphics are good
• SEO - Wordpress could be a great platform for us to work from as we already have internal experience with it and it’s easy to update. If not Wordpress, we would need something that is easy to SEO optimize
• An “our team” section with pictures
• Sell the message to potential clients why they need managed services
• Home page needs to convey our core services at a glance
• Home page needs to load quickly
• Screenshots of our monitoring and security reports
• Easy for us to update/edit certain areas
o New products
o Testimonials
Nice to have
• • Something like TW’s savings calculator - http://www.tidewarden.example/it-savings-calculator/
• Webform to enter service ticket requests
• Motion of home page banner
• Maybe pull in RSS feeds from current tech news sources
• Rotating content on all pages to keep it fresh
• “Fern-up” feature for monthly promos
Should not have
• • Should not be overly "techie" in feel.
• Not overly wordy (like current site)

```html
<!DOCTYPE html>
<html lang="en">
<head>
<meta charset="utf-8">
<title>BrightFern IT Solutions</title>
<link href="https://fonts.googleapis.com/css2?family=Oswald:wght@400;500;700&family=Arimo:wght@400;700&display=swap" rel="stylesheet">
<style>
  :root {
    --lime: #c2f24a;
    --lime-deep: #a9e03a;
    --lime-light: #d4f870;
    --ink: #111111;
    --body-text: #1a1a1a;
    --more: #6b7d16;
    --rule: #cfcfcf;
    --highlight: #ffee00;
    --white: #ffffff;
  }
  * { margin: 0; padding: 0; box-sizing: border-box; }
  html, body { width: 1200px; height: 900px; overflow: hidden; background: var(--white); }
  body { position: relative; font-family: "Arimo", Arial, sans-serif; color: var(--body-text); }

  .hero {
    position: absolute; left: 0; top: 0; width: 1200px; height: 410px;
    background: radial-gradient(ellipse 520px 260px at 600px 250px, var(--lime-light), var(--lime) 70%, var(--lime-deep));
  }
  .page-panel {
    position: absolute; left: 180px; top: 0; width: 840px; height: 900px;
    box-shadow: 0 0 14px rgba(0,0,0,0.18);
  }

  .brand { position: absolute; left: 234px; top: 18px; width: 150px; height: 132px; text-align: center; }
  .brand-mark { width: 80px; height: 80px; border-radius: 50%; background: #4fa51c; margin: 0 auto; }
  .brand-name { font-family: "Oswald", sans-serif; font-weight: 500; font-size: 26px; color: #3d8a12; line-height: 1.2; margin-top: 6px; }
  .brand-sub { font-family: "Oswald", sans-serif; font-weight: 500; font-size: 13px; color: #3d8a12; letter-spacing: 0.5px; }

  .contact-line { position: absolute; right: 246px; top: 16px; font-size: 14px; color: var(--ink); }
  .lock-icon { position: absolute; left: 970px; top: 12px; }

  .main-nav { position: absolute; left: 638px; top: 66px; display: flex; font-family: "Oswald", sans-serif; font-size: 21px; }
  .main-nav a { color: var(--ink); text-decoration: none; padding: 2px 10px; line-height: 28px; }
  .main-nav .sep { width: 3px; height: 24px; border-left: 3px dotted var(--white); margin: 4px 4px; }
  .main-nav .current { background: var(--highlight); }

  .sub-nav { position: absolute; left: 612px; top: 114px; display: flex; font-family: "Oswald", sans-serif; font-size: 15px; }
  .sub-nav a { color: var(--ink); text-decoration: none; padding: 0 10px; }
  .sub-nav .sep { border-left: 2px dotted var(--white); height: 18px; margin-top: 2px; }

  .tagline { position: absolute; left: 180px; top: 192px; width: 840px; text-align: center; font-family: "Oswald", sans-serif; font-weight: 500; font-size: 28px; color: #1b1b1b; text-shadow: 1px 2px 3px rgba(0,0,0,0.35); line-height: 57px; }

  .slide-dots { position: absolute; left: 569px; top: 371px; display: flex; gap: 10px; }
  .slide-dots span { width: 14px; height: 14px; border-radius: 50%; background: var(--white); box-shadow: 0 1px 2px rgba(0,0,0,0.3); }
  .slide-dots .active { background: var(--ink); }

  .social-tab { position: absolute; left: 1020px; top: 214px; width: 48px; height: 86px; background: rgba(255,255,255,0.25); border-radius: 0 6px 6px 0; box-shadow: 1px 1px 3px rgba(0,0,0,0.15); }
  .social-tab span { position: absolute; left: 11px; width: 24px; height: 24px; background: var(--ink); border-radius: 3px; }

  .service { position: absolute; width: 224px; }
  .service.right-col { width: 232px; }
  .service h2 { font-family: "Oswald", sans-serif; font-weight: 500; font-size: 20.5px; color: var(--ink); line-height: 30px; margin-bottom: 10px; white-space: nowrap; }
  .service p { font-size: 12.5px; line-height: 19.4px; color: var(--body-text); }
  .service .icon { float: left; margin: 2px 8px 2px 0; }
  .service .more { display: block; text-align: right; margin-top: 8px; padding-right: 6px; font-size: 12.5px; line-height: 16px; color: var(--more); text-decoration: none; }

  .rule-v { position: absolute; width: 0; border-left: 1px dotted var(--rule); }
  .rule-h { position: absolute; height: 0; border-top: 2px dotted #e0e0e0; }

  .pitch { position: absolute; left: 720px; top: 434px; width: 290px; }
  .pitch h2 { font-family: "Oswald", sans-serif; font-weight: 500; font-size: 21px; line-height: 25px; color: var(--ink); text-transform: uppercase; margin-bottom: 12px; }
  .pitch p { font-size: 13.6px; line-height: 19.4px; color: var(--body-text); }

  .footer-links { position: absolute; left: 204px; top: 872px; font-size: 12.5px; color: var(--ink); }
  .footer-links span { margin: 0 14px; }
  .copyright { position: absolute; right: 194px; top: 876px; font-size: 12.5px; color: var(--ink); }
</style>
</head>
<body>
  <div class="hero"></div>
  <div class="page-panel"></div>

  <div class="brand">
    <div class="brand-mark"></div>
    <div class="brand-name">BrightFern</div>
    <div class="brand-sub">IT SOLUTIONS</div>
  </div>

  <div class="contact-line">Toll Free: (888) 555-0142, Phone: (480) 555-0176</div>
  <svg class="lock-icon" width="16" height="20" viewBox="0 0 16 20" aria-hidden="true">
    <path d="M4 9V6a4 4 0 0 1 8 0v3" fill="none" stroke="#111" stroke-width="2.4"/>
    <rect x="1" y="9" width="14" height="10" rx="1.5" fill="#111"/>
  </svg>

  <nav class="main-nav">
    <a class="current" href="#">Home</a><i class="sep"></i>
    <a href="#">Solutions</a><i class="sep"></i>
    <a href="#">About Us</a><i class="sep"></i>
    <a href="#">Contact</a>
  </nav>
  <nav class="sub-nav">
    <a href="#">IT Consulting</a><i class="sep"></i>
    <a href="#">IT Programs</a><i class="sep"></i>
    <a href="#">IT Security</a><i class="sep"></i>
    <a href="#">Data Backup</a>
  </nav>

  <div class="tagline">
    EVERY COMPANY NEEDS TO GROW TO SURVIVE.<br>
    WE MAKE SURE TECHNOLOGY<br>
    IS READY FOR THAT GROWTH WHEN YOU ARE.
  </div>

  <div class="slide-dots"><span></span><span></span><span class="active"></span></div>

  <div class="social-tab"><span style="top:16px"></span><span style="top:48px"></span></div>

  <section class="service" style="left:204px; top:436px;">
    <h2>IT Consulting Services</h2>
    <p><span class="icon" role="img" aria-label="Consultant icon" style="display:block;width:52px;height:58px;background:#111;border-radius:26px 26px 8px 8px;"></span>Insure that your existing system receives quality service. BrightFern will troubleshoot problems, install new software or parts, and keep your system in optimal condition...</p>
    <a class="more" href="#">more...</a>
  </section>

  <section class="service right-col" style="left:455px; top:436px;">
    <h2>IT Service Programs</h2>
    <p><svg class="icon" width="62" height="62" viewBox="0 0 62 62" aria-hidden="true">
      <circle cx="20" cy="20" r="12" fill="none" stroke="#111" stroke-width="8" stroke-dasharray="5 4"/>
      <circle cx="20" cy="20" r="9" fill="none" stroke="#111" stroke-width="5"/>
      <circle cx="42" cy="42" r="15" fill="none" stroke="#111" stroke-width="9" stroke-dasharray="6 5"/>
      <circle cx="42" cy="42" r="11" fill="none" stroke="#111" stroke-width="7"/>
    </svg>The certified professionals at BrightFern will even set up remote access for staff who work outside of the office, but need access to information at their offices...</p>
    <a class="more" href="#">more...</a>
  </section>

  <section class="service" style="left:204px; top:650px;">
    <h2>Data Backup and Recovery</h2>
    <p><svg class="icon" width="50" height="54" viewBox="0 0 54 56" aria-hidden="true">
      <ellipse cx="27" cy="8" rx="25" ry="7" fill="#111"/>
      <rect x="2" y="12" width="50" height="12" rx="6" fill="#111"/>
      <rect x="2" y="27" width="50" height="12" rx="6" fill="#111"/>
      <rect x="2" y="42" width="50" height="12" rx="6" fill="#111"/>
    </svg>Standalone systems, workstations, network servers, notebooks, peripherals, replacement parts, upgrades, software,</p>
    <a class="more" href="#">more...</a>
  </section>

  <section class="service right-col" style="left:455px; top:650px;">
    <h2>Security Vulnerability Scan</h2>
    <p><svg class="icon" width="52" height="58" viewBox="0 0 52 58" aria-hidden="true">
      <path d="M26 2 L49 9 V28 C49 42 38 51 26 56 C14 51 3 42 3 28 V9 Z" fill="#111"/>
      <path d="M26 9 L42 14 V28 C42 38 35 44 26 48 C17 44 10 38 10 28 V14 Z" fill="#fff"/>
      <path d="M14 38 L38 14 L42 18 L18 42 Z" fill="#111"/>
    </svg>Assessment services provide critical information about your system hardware and software....</p>
    <a class="more" href="#">more...</a>
  </section>

  <div class="rule-v" style="left:438px; top:440px; height:172px;"></div>
  <div class="rule-v" style="left:438px; top:648px; height:166px;"></div>
  <div class="rule-v" style="left:706px; top:434px; height:382px;"></div>
  <div class="rule-h" style="left:204px; top:634px; width:216px;"></div>
  <div class="rule-h" style="left:457px; top:634px; width:228px;"></div>

  <section class="pitch">
    <h2>BrightFern can help your business harness the power of new technology, making your business fast and efficient.</h2>
    <p>In the information age of today, one must stay abreast of current technology in order to thrive. New advancements are made daily in dispersing information and collaborative computing. High-speed networks aid in the exchange of electronic information between businesses, their customers, vendors, and peers. Businesses that are quick to act and effectively implement this technology will rise to the top.</p>
  </section>

  <div class="rule-h" style="left:204px; top:862px; width:802px; border-top-width:1px;"></div>
  <div class="footer-links">Careers<span>|</span>SiteMap</div>
  <div class="copyright">Copyright © 2012 BrightFern</div>
</body>
</html>
```